INCREASED BUDGET -- Cover Art Template Needed For Record Label

We are an electronic music record label that needs a cover art template for our 2017 releases. The design must be easy to update in Photoshop with different text, colors, or patterns.

The winner will also be asked to design our social media banners for Facebook, Twitter, and SoundCloud, so there's an opportunity to make more money.

Words to describe our sound: sophisticated, forward-thinking, futuristic, modern, emotional

Please make the HA logo the focal point of your design. Feel free to modify our logo as needed. Bonus points for anyone that can find a way to visually represent the word "Harborline". Examples of artwork that we found attractive are included to provide inspiration.

You can view our previous releases by clicking on any of the links: https://www.trackvendor-example.com/label/harborline-audio/52741/releases

Target Market(s)

Electronic music lovers

Industry/Entity Type

Music Download

Font styles to use
Serif
Decorative
Other font styles liked:
• Aller Display, Aller Light

Requirements
Must have
• Harborline Audio record logo
• Name of artist: Owen Tarsley
• Title: Daybreak / Stay Close (Remixes)
Nice to have
• Tracklist:
• Stay Close (Brannok Remix)
• Daybreak (Velktone Remix)
• Catalog number: 382

```html
<!DOCTYPE html>
<html lang="en">
<head>
<meta charset="utf-8">
<title>Owen Tarsley – Daybreak / Stay Close (Remixes)</title>
<link rel="stylesheet" href="https://fonts.googleapis.com/css2?family=Righteous&family=Roboto+Condensed:wght@700&display=swap">
<style>
  :root {
    --ink: #1e1a17;
    --ribbon-red: #e4452a;
    --ribbon-cream: #f3eda6;
    --ribbon-teal: #3aa98f;
    --title-yellow: #f6f29c;
    --subtitle-teal: #2a9e88;
    --label-rust: #b4542c;
  }
  html, body {
    margin: 0;
    padding: 0;
    overflow: hidden;
    background: var(--ink);
  }
  .cover {
    position: relative;
    width: 1200px;
    height: 1200px;
    background: var(--ink);
    overflow: hidden;
  }
  .ribbon-artwork {
    position: absolute;
    inset: 0;
    width: 1200px;
    height: 1200px;
  }
  .artist-name {
    position: absolute;
    left: 0;
    right: 0;
    top: 552px;
    margin: 0;
    text-align: center;
    font-family: "Righteous", sans-serif;
    font-weight: 400;
    font-size: 78px;
    line-height: 1;
    color: var(--title-yellow);
    letter-spacing: 1px;
  }
  .release-title {
    position: absolute;
    left: 0;
    right: 0;
    top: 650px;
    margin: 0;
    text-align: center;
    font-family: "Righteous", sans-serif;
    font-weight: 400;
    font-size: 24px;
    line-height: 1;
    color: var(--subtitle-teal);
    letter-spacing: 6px;
    text-transform: uppercase;
  }
  .label-mark {
    position: absolute;
    right: 44px;
    bottom: 44px;
    display: flex;
    flex-direction: column;
    align-items: flex-end;
    gap: 8px;
    font-family: "Roboto Condensed", sans-serif;
    font-weight: 700;
    color: var(--label-rust);
    text-transform: uppercase;
  }
  .label-name {
    display: flex;
    align-items: center;
    gap: 14px;
  }
  .label-square {
    width: 56px;
    height: 56px;
    background: var(--label-rust);
  }
  .label-words {
    display: flex;
    flex-direction: column;
    font-size: 30px;
    line-height: 1;
    letter-spacing: 0.5px;
  }
  .label-url {
    font-size: 9px;
    text-transform: none;
  }
</style>
</head>
<body>
  <main class="cover">
    <svg class="ribbon-artwork" viewBox="0 0 1200 1200" role="img" aria-label="Painted star-shaped ribbon ornament in red, cream and teal bands surrounding the title">
      <defs>
        <radialGradient id="ribbon-glow" cx="600" cy="600" r="580" gradientUnits="userSpaceOnUse">
          <stop offset="0" stop-color="#1e1a17"/>
          <stop offset="0.45" stop-color="#1e1a17"/>
          <stop offset="0.62" stop-color="#e4452a" stop-opacity="0.55"/>
          <stop offset="0.76" stop-color="#f3eda6" stop-opacity="0.5"/>
          <stop offset="0.9" stop-color="#3aa98f" stop-opacity="0.55"/>
          <stop offset="1" stop-color="#1e1a17"/>
        </radialGradient>
      </defs>
      <circle cx="600" cy="600" r="580" fill="url(#ribbon-glow)"/>
    </svg>

    <h1 class="artist-name">OWEN TARSLEY</h1>
    <p class="release-title">Daybreak / Stay Close (Remixes)</p>

    <div class="label-mark">
      <span class="label-name">
        <span class="label-square"></span>
        <span class="label-words"><span>Harborline</span><span>Audio</span></span>
      </span>
      <span class="label-url">www.harborlineaudio-example.com</span>
    </div>
  </main>
</body>
</html>
```